Powerpoint design template for FLOMBIRT for new digital platform

We would like to use a PowerPoint template, we would like to create a new page, we would like to create a new digital platform FLOMBIRT for schools and parents for the creation of playful communication and educational tools for children to enhance their positive development, amaze them learn in a playful way. This platform is going to be the most creative, stimulating and innovative classroom, easy to use and fast to implement. Scrapbooking, collages ... Magazine, newsletters Diplomla / awards Slideshows Facebook Calendars Organizers Greetings Games ... This powerpoint template will be used essential to We are looking for a professional design, positioning our brand in the children market with an adult hearing. so you will need to find a good deal. Primary target: nurseries & schools from 0 to 18 years old and universities (in 2nd phase) Secondary target: small & medium businesses Third target: general public, and TPE If it is a color scheme, then it is suggested that it be marketed in Europe (UK, Italy, Spain) and in a 2nd Stage USA and other countries. multiple options for front page, insidious pages (multiple styles with limited text and extended text) and final contact page We need something to read, we can not do it too much, but we can not do it. , and inside pages aligned to our logo

Target Market(s)

Target 1; Education with teacher Target 2; parents and grandparents

Industry/Entity Type

Education

Font styles to use
Other font styles liked:
• not decided. but not too fancy

Requirements
Must have
• Multi page options for front page, page insides (multiple styles with limited text and extended text) and final page contact
Nice to have
• do not have a lot of ideas. We need something to read, we can not get away from it
Should not have
• not too fancy and busy: keep clarity & simplicity while reassuring on quality

```html
<!DOCTYPE html>
<html lang="en">
<head>
<meta charset="utf-8">
<title>FLOMBIRT – Presentation Template, Inside Pages</title>
<link rel="stylesheet" href="https://fonts.googleapis.com/css2?family=Open+Sans:wght@400;600;700&family=Comic+Neue:wght@400;700&display=swap">
<style>
  :root {
    --backdrop: #e5e5e5;
    --page: #ffffff;
    --brand-blue: #2e9fe0;
    --brand-lime: #c6d82b;
    --ink: #2b2b2b;
    --on-blue: #ffffff;
  }
  * { box-sizing: border-box; margin: 0; padding: 0; }
  html, body {
    width: 1200px; height: 1200px; overflow: hidden;
    background: var(--backdrop);
  }
  .stage {
    position: relative; width: 1500px; height: 1500px;
    transform: scale(0.8); transform-origin: 0 0;
    font-family: "Open Sans", sans-serif;
  }
  .slide {
    position: absolute; width: 700px; height: 394px;
    background: var(--page);
    box-shadow: 1px 2px 3px rgba(0,0,0,0.35);
    overflow: hidden;
  }
  .slide--8  { left: 26px;  top: 67px; }
  .slide--9  { left: 770px; top: 67px; }
  .slide--10 { left: 26px;  top: 523px; }
  .slide--11 { left: 770px; top: 523px; }

  .slide__headline {
    position: absolute; left: 53px; top: 36px;
    color: var(--brand-blue); font-weight: 600; font-size: 21px;
  }
  .slide__rule { position: absolute; left: 0; height: 3px; }
  .slide__rule--lime { top: 69px; width: 440px; background: var(--brand-lime); }
  .slide__rule--blue { top: 76px; width: 477px; background: var(--brand-blue); }

  .brand-mark {
    position: absolute; left: 566px; top: 30px;
    display: flex; align-items: center; gap: 6px;
    color: var(--brand-blue); font-weight: 700; font-size: 19px;
  }
  .brand-mark__square { width: 14px; height: 14px; background: var(--brand-lime); }

  .rows { position: absolute; left: 0; top: 92px; width: 100%; }
  .row { position: absolute; left: 0; width: 100%; height: 62px; }
  .row:nth-child(1) { top: 0; }
  .row:nth-child(2) { top: 69px; }
  .row:nth-child(3) { top: 138px; }
  .row:nth-child(4) { top: 207px; }
  .row__label {
    position: absolute; left: 42px; top: 0; width: 20px; height: 62px;
    display: flex; align-items: center; justify-content: center;
    writing-mode: vertical-rl; transform: rotate(180deg);
    color: var(--brand-blue); font-size: 12px; letter-spacing: 1.5px;
  }
  .row__box {
    position: absolute; left: 68px; top: 0; width: 142px; height: 62px;
    background: var(--brand-blue); color: var(--on-blue);
    display: flex; align-items: center; justify-content: center;
    text-align: center; font-size: 10.5px; line-height: 14px; padding: 0 10px;
  }
  .row__text {
    position: absolute; left: 222px; top: 10px; width: 380px;
    color: var(--ink); font-size: 10.5px; line-height: 14px;
  }

  .slide__footer-rule {
    position: absolute; left: 0; top: 370px; width: 100%; height: 1.5px;
    background: var(--brand-lime);
  }
  .slide__footer {
    position: absolute; left: 0; top: 377px; width: 100%;
    color: var(--brand-blue); font-size: 8px;
  }
  .slide__footer span { position: absolute; }
  .footer__date { left: 53px; }
  .footer__label { left: 350px; transform: translateX(-50%); }
  .footer__page { left: 641px; }

  /* Variant: playful type */
  .slide--9 .row__box, .slide--9 .row__text { font-family: "Comic Neue", sans-serif; font-weight: 700; }
  .slide--9 .row__box { font-size: 11.5px; letter-spacing: 0.3px; }
  .slide--9 .row__text { font-weight: 400; font-size: 10.5px; width: 390px; top: 13px; line-height: 12.5px; font-weight: 700; }
  .slide--9 .row__label { font-size: 13px; letter-spacing: 2px; }
  .slide--9 .slide__headline { font-size: 22px; }
  .slide--9 .slide__footer { font-size: 10px; letter-spacing: 1px; }

  /* Variant: bold emphasis */
  .slide--10 .slide__headline { font-size: 24px; font-weight: 700; letter-spacing: 0.6px; top: 38px; }
  .slide--10 .row__label { font-size: 14px; font-weight: 700; letter-spacing: 2px; }
  .slide--10 .row__box { font-size: 11px; line-height: 12.5px; }
  .slide--10 .row__text { font-size: 11px; line-height: 12.5px; top: 13px; width: 390px; }
  .slide--10 .slide__footer { font-size: 11px; font-weight: 700; letter-spacing: 0.6px; }
  .slide--10 .footer__page { left: 632px; }

  /* Variant: calm */
  .slide--11 .slide__headline { font-size: 24px; letter-spacing: 0.6px; top: 38px; }
  .slide--11 .row__label { font-size: 13px; letter-spacing: 2px; }
  .slide--11 .row__box { font-size: 10px; line-height: 12.5px; }
  .slide--11 .row__text { font-size: 10.5px; line-height: 12.5px; top: 13px; width: 385px; }
  .slide--11 .slide__footer { font-size: 10px; letter-spacing: 0.6px; }
  .slide--11 .footer__page { left: 634px; }
</style>
</head>
<body>
<main class="stage">

  <section class="slide slide--8">
    <h1 class="slide__headline">Headline</h1>
    <div class="slide__rule slide__rule--lime"></div>
    <div class="slide__rule slide__rule--blue"></div>
    <div class="brand-mark"><span class="brand-mark__square"></span>FLOMBIRT</div>
    <div class="rows">
      <div class="row"><span class="row__label">Title</span><div class="row__box">Lorem ipsum dolor sit amet, consetetur sadipscing elitr</div><p class="row__text">Lorem ipsum dolor sit amet, consetetur sadipscing elitr, sed diam nonumy eirmod tempor invidunt ut labore et dolore magna aliquyam erat, sed diam voluptua. At vero eos et accusam et justo duo dolores et ea rebum.</p></div>
      <div class="row"><span class="row__label">Title</span><div class="row__box">Lorem ipsum dolor sit amet, consetetur sadipscing elitr</div><p class="row__text">Lorem ipsum dolor sit amet, consetetur sadipscing elitr, sed diam nonumy eirmod tempor invidunt ut labore et dolore magna aliquyam erat, sed diam voluptua. At vero eos et accusam et justo duo dolores et ea rebum.</p></div>
      <div class="row"><span class="row__label">Title</span><div class="row__box">Lorem ipsum dolor sit amet, consetetur sadipscing elitr</div><p class="row__text">Lorem ipsum dolor sit amet, consetetur sadipscing elitr, sed diam nonumy eirmod tempor invidunt ut labore et dolore magna aliquyam erat, sed diam voluptua. At vero eos et accusam et justo duo dolores et ea rebum.</p></div>
      <div class="row"><span class="row__label">Title</span><div class="row__box">Lorem ipsum dolor sit amet, consetetur sadipscing elitr</div><p class="row__text">Lorem ipsum dolor sit amet, consetetur sadipscing elitr, sed diam nonumy eirmod tempor invidunt ut labore et dolore magna aliquyam erat, sed diam voluptua. At vero eos et accusam et justo duo dolores et ea rebum.</p></div>
    </div>
    <div class="slide__footer-rule"></div>
    <footer class="slide__footer"><span class="footer__date">12.11.16</span><span class="footer__label">FOOTER</span><span class="footer__page">8</span></footer>
  </section>

  <section class="slide slide--9">
    <h1 class="slide__headline">Headline</h1>
    <div class="slide__rule slide__rule--lime"></div>
    <div class="slide__rule slide__rule--blue"></div>
    <div class="brand-mark"><span class="brand-mark__square"></span>FLOMBIRT</div>
    <div class="rows">
      <div class="row"><span class="row__label">Title</span><div class="row__box">Lorem ipsum dolor sit amet, consetetur sadipscing elitr</div><p class="row__text">Lorem ipsum dolor sit amet, consetetur sadipscing elitr, sed diam nonumy eirmod tempor invidunt ut labore et dolore magna aliquyam erat, sed diam voluptua. At vero eos et accusam et justo duo dolores et ea rebum.</p></div>
      <div class="row"><span class="row__label">Title</span><div class="row__box">Lorem ipsum dolor sit amet, consetetur sadipscing elitr</div><p class="row__text">Lorem ipsum dolor sit amet, consetetur sadipscing elitr, sed diam nonumy eirmod tempor invidunt ut labore et dolore magna aliquyam erat, sed diam voluptua. At vero eos et accusam et justo duo dolores et ea rebum.</p></div>
      <div class="row"><span class="row__label">Title</span><div class="row__box">Lorem ipsum dolor sit amet, consetetur sadipscing elitr</div><p class="row__text">Lorem ipsum dolor sit amet, consetetur sadipscing elitr, sed diam nonumy eirmod tempor invidunt ut labore et dolore magna aliquyam erat, sed diam voluptua. At vero eos et accusam et justo duo dolores et ea rebum.</p></div>
      <div class="row"><span class="row__label">Title</span><div class="row__box">Lorem ipsum dolor sit amet, consetetur sadipscing elitr</div><p class="row__text">Lorem ipsum dolor sit amet, consetetur sadipscing elitr, sed diam nonumy eirmod tempor invidunt ut labore et dolore magna aliquyam erat, sed diam voluptua. At vero eos et accusam et justo duo dolores et ea rebum.</p></div>
    </div>
    <div class="slide__footer-rule"></div>
    <footer class="slide__footer"><span class="footer__date">12.11.16</span><span class="footer__label">FOOTER</span><span class="footer__page">9</span></footer>
  </section>

  <section class="slide slide--10">
    <h1 class="slide__headline">Headline</h1>
    <div class="slide__rule slide__rule--lime"></div>
    <div class="slide__rule slide__rule--blue"></div>
    <div class="brand-mark"><span class="brand-mark__square"></span>FLOMBIRT</div>
    <div class="rows">
      <div class="row"><span class="row__label">Title</span><div class="row__box">Lorem ipsum dolor sit amet, consetetur sadipscing elitr</div><p class="row__text">Lorem ipsum dolor sit amet, consetetur sadipscing elitr, sed diam nonumy eirmod tempor invidunt ut labore et dolore magna aliquyam erat, sed diam voluptua. At vero eos et accusam et justo duo dolores et ea rebum.</p></div>
      <div class="row"><span class="row__label">Title</span><div class="row__box">Lorem ipsum dolor sit amet, consetetur sadipscing elitr</div><p class="row__text">Lorem ipsum dolor sit amet, consetetur sadipscing elitr, sed diam nonumy eirmod tempor invidunt ut labore et dolore magna aliquyam erat, sed diam voluptua. At vero eos et accusam et justo duo dolores et ea rebum.</p></div>
      <div class="row"><span class="row__label">Title</span><div class="row__box">Lorem ipsum dolor sit amet, consetetur sadipscing elitr</div><p class="row__text">Lorem ipsum dolor sit amet, consetetur sadipscing elitr, sed diam nonumy eirmod tempor invidunt ut labore et dolore magna aliquyam erat, sed diam voluptua. At vero eos et accusam et justo duo dolores et ea rebum.</p></div>
      <div class="row"><span class="row__label">Title</span><div class="row__box">Lorem ipsum dolor sit amet, consetetur sadipscing elitr</div><p class="row__text">Lorem ipsum dolor sit amet, consetetur sadipscing elitr, sed diam nonumy eirmod tempor invidunt ut labore et dolore magna aliquyam erat, sed diam voluptua. At vero eos et accusam et justo duo dolores et ea rebum.</p></div>
    </div>
    <div class="slide__footer-rule"></div>
    <footer class="slide__footer"><span class="footer__date">12.11.16</span><span class="footer__label">FOOTER</span><span class="footer__page">10</span></footer>
  </section>

  <section class="slide slide--11">
    <h1 class="slide__headline">Headline</h1>
    <div class="slide__rule slide__rule--lime"></div>
    <div class="slide__rule slide__rule--blue"></div>
    <div class="brand-mark"><span class="brand-mark__square"></span>FLOMBIRT</div>
    <div class="rows">
      <div class="row"><span class="row__label">Title</span><div class="row__box">Lorem ipsum dolor sit amet, consetetur sadipscing elitr</div><p class="row__text">Lorem ipsum dolor sit amet, consetetur sadipscing elitr, sed diam nonumy eirmod tempor invidunt ut labore et dolore magna aliquyam erat, sed diam voluptua. At vero eos et accusam et justo duo dolores et ea rebum.</p></div>
      <div class="row"><span class="row__label">Title</span><div class="row__box">Lorem ipsum dolor sit amet, consetetur sadipscing elitr</div><p class="row__text">Lorem ipsum dolor sit amet, consetetur sadipscing elitr, sed diam nonumy eirmod tempor invidunt ut labore et dolore magna aliquyam erat, sed diam voluptua. At vero eos et accusam et justo duo dolores et ea rebum.</p></div>
      <div class="row"><span class="row__label">Title</span><div class="row__box">Lorem ipsum dolor sit amet, consetetur sadipscing elitr</div><p class="row__text">Lorem ipsum dolor sit amet, consetetur sadipscing elitr, sed diam nonumy eirmod tempor invidunt ut labore et dolore magna aliquyam erat, sed diam voluptua. At vero eos et accusam et justo duo dolores et ea rebum.</p></div>
      <div class="row"><span class="row__label">Title</span><div class="row__box">Lorem ipsum dolor sit amet, consetetur sadipscing elitr</div><p class="row__text">Lorem ipsum dolor sit amet, consetetur sadipscing elitr, sed diam nonumy eirmod tempor invidunt ut labore et dolore magna aliquyam erat, sed diam voluptua. At vero eos et accusam et justo duo dolores et ea rebum.</p></div>
    </div>
    <div class="slide__footer-rule"></div>
    <footer class="slide__footer"><span class="footer__date">12.11.16</span><span class="footer__label">FOOTER</span><span class="footer__page">11</span></footer>
  </section>

</main>
</body>
</html>
```